WordPress design needed for scientist

Hi! I am a female scientist (36 years old) in the field of marine science and biotechnology. I need a clean, engaging, modern WordPress website design. Not just a blog, but a site that shows pictures of my research and topics, can host PDFs of my research publications, and can have my Chirplinefeed (@miraleventhorp) and VidTrove videos embedded. Something a bit like this: http://www.quennimore.org.uk/ but with my content, and a more engaging design, like the template "PLUME"

My current webprofile from the University of Fjeldvik is here: http://www.uof.no/personer/Mira.Ruth.Leventhorp , but I need something that is more than this, that can inspire grant evaluators to pick me, and a website that shows the best sides of me and my research. I attach some representative pictures of me and my research that I would like to be used/incorporated in the webdesign.

Target Market(s)

other scientists, journalists, media, interested members of the public

Industry/Entity Type

Biotechnology

Font styles to use
Sans Serif

Requirements
Must have
• VidTrove video embedding of these videos:
• https://www.vidtrove.example/watch?v=Q7KPLMZTwe3
• https://www.vidtrove.example/watch?v=ht4bRcNpaXs
• https://www.vidtrove.example/watch?v=Ze9KUwdqYrB
• Slidora Presentations embedded: https://slidora.example/user/miraleventhorp/

```html
<!DOCTYPE html>
<html lang="en">
<head>
<meta charset="utf-8">
<title>Research – Mira Ruth Leventhorp</title>
<link href="https://fonts.googleapis.com/css2?family=Open+Sans:wght@400;600;700&family=Playfair+Display:wght@400;700&display=swap" rel="stylesheet">
<style>
:root{
  --ink:#4a3128;
  --body:#3b3533;
  --accent:#c0504d;
  --accent-soft:#e7a9a6;
  --muted:#9b9391;
  --blush:#f9ebe8;
  --blush-deep:#f2dedb;
  --white:#ffffff;
}
*{margin:0;padding:0;box-sizing:border-box}
html,body{width:797px;height:1200px;overflow:hidden;background:var(--white)}
body{position:relative;font-family:"Open Sans",sans-serif;color:var(--body)}
.abs{position:absolute}
.site-header{left:0;top:0;width:797px;height:33px;background:var(--white)}
.brand{left:168px;top:10px;font-family:"Playfair Display",serif;font-weight:700;font-size:10px;color:var(--ink);letter-spacing:.5px}
.main-nav{top:14px;left:0;width:797px;font-size:5.2px;letter-spacing:.4px;color:var(--muted);text-transform:uppercase}
.main-nav span{position:absolute;white-space:nowrap}
.main-nav .current{color:var(--accent)}
.page-hero{left:0;top:33px;width:797px;height:83px;background:var(--blush)}
.page-title{left:207px;top:48px;font-family:"Playfair Display",serif;font-weight:400;font-size:21px;color:var(--ink)}
.hero-rule{left:207px;top:83px;width:34px;height:1px;background:var(--accent)}
.hero-lede{left:247px;top:79px;width:172px;font-size:6.2px;line-height:10px;color:var(--accent)}
.section-label{left:168px;top:158px;font-size:5.6px;font-weight:700;letter-spacing:.5px;color:var(--muted);text-transform:uppercase}
.thumb{position:absolute;left:168px;width:145px}
.entry-title{position:absolute;font-family:"Playfair Display",serif;font-weight:700;font-size:13.5px;line-height:15px;color:var(--ink)}
.entry-text{position:absolute;font-size:6.1px;line-height:10px;color:var(--body)}
.read-more{position:absolute;height:19px;border:1px solid var(--accent-soft);font-size:5.2px;color:var(--accent);text-transform:uppercase;letter-spacing:.3px;display:flex;align-items:center;justify-content:center}
.site-footer{left:0;top:911px;width:797px;height:246px;background:var(--blush)}
.footer-label{position:absolute;top:952px;font-size:6px;font-weight:700;color:var(--accent);letter-spacing:.5px;text-transform:uppercase}
.contact-block{position:absolute;font-size:6.1px;line-height:7.5px;color:var(--body)}
.contact-block b{font-weight:700;letter-spacing:.4px;display:block}
.contact-block .link{color:var(--accent)}
.feed{left:405px;top:972px;width:184px;height:140px;background:var(--white);border:1px solid #e3e3e3;font-family:Arial,sans-serif;font-size:5.2px;color:#333;overflow:hidden}
.feed-head{height:18px;border-bottom:1px solid #eee;display:flex;align-items:center;justify-content:space-between;padding:0 4px}
.feed-head strong{font-size:7.5px}
.follow{border:1px solid #ccc;border-radius:2px;padding:1px 3px;font-size:4.6px;font-weight:700;background:#f4f4f4}
.post{position:relative;padding:4px 4px 4px 27px;border-bottom:1px solid #eee;line-height:6.3px}
.avatar{position:absolute;left:4px;top:5px;width:19px;height:19px;border-radius:2px}
.post .date{position:absolute;right:4px;top:4px;color:#888}
.post .handle{color:#888;font-weight:400}
.post a{color:var(--accent);text-decoration:none}
.post .meta{color:#777;font-size:4.6px}
.feed-base{left:405px;top:1096px;width:184px;height:16px;background:#eceaea}
.feed-compose{position:absolute;left:410px;top:1098px;width:175px;height:10px;border:1px solid #ddd;font-size:4.8px;padding:1px 3px;color:#555;background:#fff}
.site-bottom{left:0;top:1157px;width:797px;height:43px;background:var(--blush-deep)}
.copyright{left:168px;top:1175px;font-size:6px;color:#c5a7a3}
</style>
</head>
<body>

<header class="abs site-header">
  <div class="abs brand">MRL</div>
  <nav class="abs main-nav">
    <span style="left:348px">Home</span>
    <span class="current" style="left:378px">Research</span>
    <span style="left:415px">Videos</span>
    <span style="left:445px">Lectures</span>
    <span style="left:483px">Publications</span>
    <span style="left:527px">Qualifications</span>
    <span style="left:580px">Current Projects</span>
  </nav>
</header>

<section class="abs page-hero"></section>
<h1 class="abs page-title">Research</h1>
<div class="abs hero-rule"></div>
<p class="abs hero-lede">Class aptent taciti sociosqu ad litora torquent per conubia nostra, per inceptos himenaeos.</p>

<div class="abs section-label">Featured research</div>

<div class="thumb" style="top:182px;height:87px;background:linear-gradient(180deg,#8c3e22,#a8532e 40%,#7a3318)" role="img" aria-label="Close-up photo of reddish-brown marine sediment"></div>
<h2 class="entry-title" style="left:326px;top:180px">Naturforvaltning</h2>
<p class="entry-text" style="left:326px;top:201px;width:230px">Aenean convallis tempus turpis a lacinia. Fusce consectetur lorem lorem, porttitor imperdiet felis vestibulum ut. Nullam ex ipsum, gravida eget bibendum in, pellentesque non ligula. Nunc ac euismod turpis, et consequat risus.</p>
<div class="read-more" style="left:326px;top:251px;width:67px">Read more</div>

<div class="thumb" style="top:311px;height:83px;background:linear-gradient(180deg,#8f9190,#b5b3a6 50%,#6f7a5e)" role="img" aria-label="Photo of round aquaculture tanks at a research station"></div>
<h2 class="entry-title" style="left:326px;top:308px">Populasjonsdynamikk &nbsp;(matematiskemodeller)</h2>
<p class="entry-text" style="left:326px;top:332px;width:220px">Nulla pharetra dapibus iaculis. Aenean non tempor lorem. Praesent cursus ullamcorper velit eget maximus. Aenean eu est ut nunc efficitur semper a non felis. Nulla in eros ligula.</p>
<div class="read-more" style="left:326px;top:375px;width:67px">Read more</div>

<div class="thumb" style="top:436px;height:82px;background:linear-gradient(135deg,#f2ea5a,#e6d23a 45%,#c8452f 75%,#4e8a3e)" role="img" aria-label="Annotated habitat map of a coastal region"></div>
<h2 class="entry-title" style="left:326px;top:433px;width:240px">Tverfagelige studier innen fornybarressursforvaltning</h2>
<p class="entry-text" style="left:326px;top:470px;width:220px">Nulla pharetra dapibus iaculis. Aenean non tempor lorem. Praesent cursus ullamcorper velit eget maximus.</p>
<div class="read-more" style="left:326px;top:500px;width:67px">Read more</div>

<h2 class="entry-title" style="left:247px;top:557px">Science/policy interface</h2>
<p class="entry-text" style="left:247px;top:580px;width:340px">Nulla pharetra dapibus iaculis. Aenean non tempor lorem. Praesent cursus ullamcorper velit eget maximus.</p>
<div class="read-more" style="left:247px;top:610px;width:67px">Read more</div>

<h2 class="entry-title" style="left:247px;top:668px;width:340px">1109 Forsker i prosjektet "Adaptive Ocean Modelling", Senter for Kunnskapsfilosofi (SKF), UoF</h2>
<p class="entry-text" style="left:247px;top:703px;width:340px">Nulla pharetra dapibus iaculis. Aenean non tempor lorem. Praesent cursus ullamcorper velit eget maximus.</p>
<div class="read-more" style="left:247px;top:720px;width:67px">Read more</div>

<h2 class="entry-title" style="left:247px;top:778px;width:340px">Postdoc i prosjektet "HAVRO: Resilient Governance of Coastal Fisheries" ved Havkunnskapsinstituttet, Fjeldvik</h2>
<p class="entry-text" style="left:247px;top:834px;width:340px">Nulla pharetra dapibus iaculis. Aenean non tempor lorem. Praesent cursus ullamcorper velit eget maximus.</p>
<div class="read-more" style="left:247px;top:852px;width:67px">Read more</div>

<footer class="abs site-footer"></footer>
<div class="footer-label" style="left:168px">Contact</div>
<div class="footer-label" style="left:405px">Chirpline</div>

<div class="contact-block" style="left:168px;top:974px">
  <b>E-POST</b>
  <span class="link">Mira.Leventhorp@uof.no</span>
  <b style="margin-top:7px">Telefon</b>
  +47 55 41 07 32<br>+47 93 26 18 54
</div>
<div class="contact-block" style="left:286px;top:974px">
  <b>Besoksadresse</b>
  Fjordgata 12<br>Rom: 200
  <b style="margin-top:7px">Postadresse</b>
  Postboks 4410<br>5831 Fjeldvik
</div>

<div class="abs feed">
  <div class="feed-head"><strong>Posts</strong><span class="follow">Follow</span></div>
  <div class="post">
    <div class="avatar" style="background:#8a8f95" role="img" aria-label="Profile picture"></div>
    <span class="date">29 Jan</span>
    <b>Tomas Verhaegen</b> <span class="handle">@TVerhaegen</span><br>
    1986 Interview of Arne Solbakken on the Challenger Disaster.<a>m.vidtrove.example/watch?v=4kp…</a><br>
    <span class="meta">⟲ Reposted by Mira Ruth Leventhorp</span><br>
    <span class="meta">▣ Show Media</span>
  </div>
  <div class="post">
    <div class="avatar" style="background:#b98d7a" role="img" aria-label="Profile picture"></div>
    <span class="date">28 Jan</span>
    <b>Mira Ruth Leventhorp</b> <span class="handle">@miraleventhorp</span><br>
    Yay! <a>@kariholmstad</a> and <a>@paulmarchetti</a> are self-declared Feminists! <a>#momentofzen chirpline.example/kariholmst…</a><br>
    <span class="meta">⌖ Fjeldvik, Norway, Norge</span>
  </div>
  <div class="post" style="border:none">
    <div class="avatar" style="background:#b98d7a" role="img" aria-label="Profile picture"></div>
    <span class="date">27 Jan</span>
    <b>Mira Ruth Leventhorp</b> <span class="handle">@miraleventhorp</span><br>
    Excellent Slidora on the power of the narrative to inspire, teach and motivate! <a>slidora.example/vlq…</a>
  </div>
</div>
<div class="abs feed-base"></div>
<div class="feed-compose">Post to @miraleventhorp</div>

<div class="abs site-bottom"></div>
<div class="abs copyright">Copyright 2016. Mira Ruth Leventhorp.</div>

</body>
</html>
```